Breezeway Climate Business Card Design

Design new, 2 sides, business cards for a residential and light commercial heating, air conditioning contractor.

Target Market(s)

Homeowners, small businesses

Industry/Entity Type

Business

Contact Information for Business Card

Dominic Vasquerelli
Phone - 555-214-6837
Email
Address - PO box 618
Millbrook NJ 07999
Website - www.BreezewayClimateLLC.example

Requirements
Must have
• logo, company colors, standard size with no die cut, so I can use printhaven

```html
<!DOCTYPE html>
<html lang="en">
<head>
<meta charset="utf-8">
<title>Breezeway Climate Business Card</title>
<link href="https://fonts.googleapis.com/css2?family=Montserrat:wght@400;600;700&display=swap" rel="stylesheet">
<style>
  :root {
    --charcoal: #2b2b2b;
    --orange: #ef8630;
    --cream: #fff4b5;
    --ink: #3b2a1f;
    --white: #ffffff;
    --page: #ffffff;
  }
  * { margin: 0; padding: 0; box-sizing: border-box; }
  html, body {
    width: 1007px; height: 1200px; overflow: hidden;
    background: var(--page);
    font-family: "Montserrat", Arial, sans-serif;
  }
  .canvas { position: relative; width: 1007px; height: 1200px; }
  .card {
    position: absolute; left: 152px; width: 717px; height: 425px;
    background: var(--orange); overflow: hidden;
    box-shadow: 0 18px 40px rgba(0,0,0,0.35);
  }
  .card--front { top: 135px; }
  .card--back { top: 656px; }
  .card__band { position: absolute; left: 0; top: 0; width: 100%; background: var(--charcoal); }
  .card--front .card__band { height: 220px; }
  .card--back .card__band { height: 179px; }
  .card__rule { position: absolute; left: 0; top: 179px; width: 100%; height: 4px; background: var(--cream); }

  .brand-name {
    position: absolute; color: var(--cream); font-weight: 700;
    text-transform: uppercase; line-height: 1.05;
    display: flex; align-items: center;
  }
  .brand-name__dot { border-radius: 50%; background: var(--cream); flex: none; }
  .brand-name__words { display: flex; flex-direction: column; }

  .card--front .brand-name { left: 0; width: 100%; top: 88px; justify-content: center; gap: 22px; font-size: 50px; letter-spacing: 2px; }
  .card--front .brand-name__dot { width: 40px; height: 40px; }

  .card--back .brand-name { left: 30px; top: 76px; gap: 10px; font-size: 22px; letter-spacing: 1px; }
  .card--back .brand-name__dot { width: 18px; height: 18px; }

  .holder { position: absolute; left: 254px; top: 100px; width: 200px; text-align: center; color: var(--white); }
  .holder__name { font-weight: 700; font-size: 21px; white-space: nowrap; margin-left: -30px; margin-right: -30px; }
  .holder__role { font-weight: 400; font-size: 22px; color: #f1ead0; margin-top: 2px; }

  .contacts { position: absolute; left: 242px; top: 211px; list-style: none; }
  .contacts li { display: flex; align-items: center; height: 34.3px; font-size: 19px; color: var(--ink); white-space: nowrap; }
  .contacts svg { width: 24px; height: 24px; margin-right: 9px; flex: none; }
</style>
</head>
<body>
<main class="canvas">
  <section class="card card--front" aria-label="Business card front">
    <div class="card__band"></div>
    <div class="brand-name">
      <span class="brand-name__dot"></span>
      <span class="brand-name__words"><span>Breezeway</span><span>Climate</span></span>
    </div>
  </section>

  <section class="card card--back" aria-label="Business card back">
    <div class="card__band"></div>
    <div class="card__rule"></div>
    <div class="brand-name">
      <span class="brand-name__dot"></span>
      <span class="brand-name__words"><span>Breezeway</span><span>Climate</span></span>
    </div>
    <div class="holder">
      <p class="holder__name">Dominic Vasquerelli</p>
      <p class="holder__role">Owner</p>
    </div>
    <ul class="contacts">
      <li>
        <svg viewBox="0 0 24 24" fill="none" stroke="#fff" stroke-width="1.8"><path d="M6 3l3 1 1 4-2 2c1 3 3 5 6 6l2-2 4 1 1 3-2 3C11 21 3 13 3 6z"/></svg>
        555-214-6837
      </li>
      <li>
        <svg viewBox="0 0 24 24" fill="none" stroke="#fff" stroke-width="1.8"><path d="M12 22s-7-7-7-12a7 7 0 0 1 14 0c0 5-7 12-7 12z"/><circle cx="12" cy="10" r="2.5"/></svg>
        PO box 618, Millbrook NJ 07999
      </li>
      <li>
        <svg viewBox="0 0 24 24" fill="none" stroke="#fff" stroke-width="1.8"><rect x="2" y="6" width="20" height="13" rx="1"/><path d="M2 7l10 7 10-7"/></svg>
        info@BreezewayClimateLLC.example
      </li>
      <li>
        <svg viewBox="0 0 24 24" fill="none" stroke="#fff" stroke-width="1.6"><circle cx="12" cy="12" r="10"/><ellipse cx="12" cy="12" rx="4.5" ry="10"/><line x1="2" y1="12" x2="22" y2="12"/><path d="M4 7h16M4 17h16"/></svg>
        www.BreezewayClimateLLC.example
      </li>
    </ul>
  </section>
</main>
</body>
</html>
```